Plakat-Design
Zielgruppe
Kosmetikstudio zur Haarentfernung mit Waxing und Sugaring (handwerklich, keine IPL/Lasergeräte).
Angeboten wird die Enthaarung des gesamten Körpers
Am häufigsten gebuchte Behandlung: Brazilian Cut (Enthaarung Intimbereich), gefolgt von Beinen, Achseln und Augenbrauen
Zielgruppe:
Ca. 80% weiblich
Ca. 20% Männer (hauptsächlich Rücken-Enthaarung)
Hauptzielgruppe: 25 bis 35 Jahre, weiblich, interessiert an Schönheit, Mode, Wellness, insgesamt
Werte und Vision:
Spezialisiert: Dadurch, dass wir uns auf eine Sache (im Gegensatz des gesamten Kosmetik-Spektrums) konzentrieren, können wir unseren Kunden einen Service bieten der:
* besonders professionell, schnell, unkompliziert ist und zu einem fairen Preis
Dabei sind für uns folgende Werte besonders wichtig:
* Freundlichkeit, Entspannte Atmosphäre & gutes Miteinander im Team, Professionalität der Service-Qualität
Wir sind das erste Waxing Studio in Trier mit
* >10 Jahren Erfahrung
* > 6.000 zufriedenen Kunden
* > 90.000 professionellen Behandlungen
Mehr Infos auf unserer Website: www.glattora.de
Aufgabenstellung
Zu gestalten sind 5 große Schaufenster. 2 befinden sich an einer Straße, an der Autos vorbei fahren, 3 in der Fußgängerzone. Die Größe der Fenster ist 165x220 cm (BreitexHöhe). Siehe Fotos: Die Größe der Fenster bezieht sich auf jeweils das große Fenster ohne die beiden kleinen Oberlichter.
Wir wünschen uns ein langfristiges Design, das unsere Kunden anspricht und unsere große Werbefläche optimal nutzt.
Wir wünschen uns, dass das Design die oben beschriebene Stimmung vermittelt, unsere langjährige Professionalität, Freundlichkeit, Kundenorientierung, Spaß an der Arbeit/im Studio ....
Wichtig ist auch der Sichtschutz. Da wir körpernah arbeiten und sich hinter den Schaufenstern Kabinen befinden, benötigen wir 100% Sichtschutz. Derzeit sind innenseitig Gardinen angebracht, die Sichtschutz bieten. Die Schaufenstergestaltung könnte zwischen Gardinen und Fenster angebracht werden oder die Gardinen könnten entfernt werden, dann müsste die Schaufenstergestaltung den Sichtschutz bieten.
Die Stadt Trier hat eine Werbesatzung, die einzuhalten ist, ggf. Genehmigung bedarf: https://www.beispielstadt-verwaltung.de/wirtschaft-arbeit/einzelhandel/werbesatzung/
Am einfachsten wäre es, die Werbung innen mit einem Abstand von mind. 10cm zum Fenster anzubringen, um die Werbesatzung zu umgehen. z.B. Banner im Schaufenster. Bei einer Beklebung der Fenster müsste eine Genehmigung angefragt werden.

```html
<!DOCTYPE html>
<html lang="de">
<head>
<meta charset="utf-8">
<title>Glattora – Schaufenster</title>
<link href="https://fonts.googleapis.com/css2?family=Nunito:wght@800;900&family=Montserrat:wght@400;500;600&display=swap" rel="stylesheet">
<style>
  :root {
    --teal-dark: #0b5868;
    --teal-deep: #0d6677;
    --teal-mid: #0f8c93;
    --teal-light: #14aaa9;
    --teal-pale: #cdeeee;
    --grey-text: #7a7a7a;
    --white: #ffffff;
  }
  * { margin: 0; padding: 0; box-sizing: border-box; }
  html, body { width: 1200px; height: 320px; overflow: hidden; background: var(--white); }
  .windows { position: relative; width: 1200px; height: 320px; display: flex; }
  .window { position: relative; width: 240px; height: 320px; overflow: hidden; }
  .heading { font-family: "Nunito", sans-serif; font-weight: 900; }
  .body { font-family: "Montserrat", sans-serif; }

  /* Window 1 */
  .window--since { background: var(--white); }
  .window--since .dots { position: absolute; inset: 0; }
  .bulb-area { position: absolute; left: 51px; top: 55px; width: 138px; height: 205px; border-radius: 69px 69px 24px 24px; background: radial-gradient(ellipse at 50% 35%, #e6f6f6 0%, #f3fbfb 55%, #ffffff 100%); }
  .since-text { position: absolute; left: 68px; top: 92px; width: 104px; text-align: center; }
  .since-year { color: var(--teal-dark); font-size: 17px; }
  .since-year small { font-size: 8px; margin-right: 3px; }
  .since-copy { color: var(--grey-text); font-size: 9.6px; line-height: 13.6px; margin-top: 6px; }

  /* Window 2 */
  .photo { position: absolute; inset: 0; }
  .photo--studio { background: linear-gradient(160deg, #e8eaea 0%, #cfd4d4 45%, #2a3a3c 70%, #16807f 100%); }
  .claim-box { position: absolute; left: 37px; top: 158px; width: 173px; height: 99px; background: rgba(255,255,255,0.85); border-bottom: 3px solid var(--teal-light); }
  .claim-box p { color: var(--teal-dark); font-size: 16.5px; line-height: 22px; text-align: center; margin-top: 13px; }
  .brand-badge { position: absolute; border-radius: 50%; background: linear-gradient(150deg, var(--teal-light), var(--teal-deep)); display: flex; align-items: center; justify-content: center; }
  .brand-badge span { font-family: "Montserrat", sans-serif; font-weight: 600; color: var(--white); font-size: 13px; }
  .window--claim .brand-badge { left: 89px; top: 224px; width: 71px; height: 71px; }

  /* Window 3 */
  .window--facts { background: linear-gradient(90deg, var(--teal-light) 0%, var(--teal-mid) 35%, var(--teal-dark) 100%); color: var(--white); }
  .facts-title { position: absolute; top: 30px; width: 100%; text-align: center; font-size: 16px; letter-spacing: 0.3px; }
  .fact { position: absolute; left: 0; width: 240px; height: 60px; }
  .fact svg { position: absolute; left: 36px; top: 0; }
  .fact-text { position: absolute; left: 91px; }
  .fact-value { font-size: 19px; line-height: 20px; }
  .fact-value small { font-size: 10px; }
  .fact-label { font-size: 6.6px; letter-spacing: 0.3px; margin-top: 5px; font-weight: 500; }
  .fact-label--plain { letter-spacing: 0.1px; }
  .divider { position: absolute; left: 19px; width: 202px; height: 1px; background: rgba(255,255,255,0.75); }

  /* Window 4 */
  .photo--treatment { background: linear-gradient(170deg, #f2f2f2 0%, #dcdcdc 40%, #1d2628 65%, #e8e8e8 100%); }
  .wax-badge { position: absolute; }
  .window--welcome .wax-badge { left: 102px; top: 9px; }
  .wax-badge-core { position: absolute; left: 14px; top: 14px; width: 100px; height: 100px; border-radius: 50%; background: var(--teal-dark); border: 3px solid var(--teal-light); display: flex; align-items: center; justify-content: center; text-align: center; }
  .wax-badge-core p { color: var(--white); font-size: 21px; line-height: 21px; }

  /* Window 5 */
  .window--smooth { background: var(--white); }
  .smooth-title { position: absolute; top: 30px; width: 100%; text-align: center; color: var(--teal-dark); font-size: 16.5px; line-height: 22px; }
  .photo--friends { position: absolute; left: 30px; top: 102px; width: 240px; height: 240px; border-radius: 50%; background: linear-gradient(140deg, #e9e3dc 0%, #c9b7a8 45%, #9aa7b2 100%); }
  .window--smooth .brand-badge { left: 19px; top: 92px; width: 75px; height: 75px; }
</style>
</head>
<body>
<main class="windows">

  <section class="window window--since">
    <svg class="dots" width="240" height="320" viewBox="0 0 240 320" aria-hidden="true">
      <g fill="var(--teal-light)">
        <circle cx="55" cy="14" r="5"/><circle cx="120" cy="31" r="1.5"/>
        <circle cx="219" cy="106" r="8" opacity=".6"/><circle cx="32" cy="179" r="3"/>
        <circle cx="204" cy="193" r="5"/><circle cx="40" cy="279" r="8" opacity=".55"/>
        <circle cx="166" cy="292" r="5"/>
      </g>
      <g fill="var(--teal-pale)">
        <circle cx="29" cy="89" r="15" opacity=".7"/><circle cx="196" cy="244" r="15" opacity=".7"/>
        <circle cx="202" cy="35" r="3" fill="#d8dcdc"/><circle cx="55" cy="221" r="3" fill="#d8dcdc"/>
      </g>
    </svg>
    <div class="bulb-area" role="img" aria-label="Illustration: Glühbirne als feine Linienzeichnung"></div>
    <div class="since-text">
      <p class="since-year heading"><small>SEIT</small>2012</p>
      <p class="since-copy body">sind wir das Erste spezialisiertes Waxing-Studio in Trier</p>
    </div>
  </section>

  <section class="window window--claim">
    <div class="photo photo--studio" role="img" aria-label="Foto: Kosmetikerin mit Maske hebt Spatel mit türkisem Wachs im Studio"></div>
    <div class="claim-box"><p class="heading">Dein Waxing-<br>Studio mit Herz</p></div>
    <div class="brand-badge"><span>glattora</span></div>
  </section>

  <section class="window window--facts">
    <h2 class="facts-title heading">UNSERE ERFAHRUNG</h2>
    <div class="fact body" style="top:83px">
      <svg width="30" height="30" viewBox="0 0 30 30" aria-hidden="true"><circle cx="14" cy="14" r="13.5" fill="none" stroke="#fff" stroke-width=".8"/><path d="M7 14 L13 21 L27 4" fill="none" stroke="#fff" stroke-width=".9"/></svg>
      <div class="fact-text" style="top:2px"><p class="fact-value heading"><small>über </small>10 Jahre</p><p class="fact-label">ERFOLGREICH IN TRIER</p></div>
    </div>
    <div class="divider" style="top:133px"></div>
    <div class="fact body" style="top:156px">
      <svg width="30" height="30" viewBox="0 0 30 30" aria-hidden="true"><circle cx="14" cy="14" r="13.5" fill="none" stroke="#fff" stroke-width=".8"/><path d="M7 14 L13 21 L27 4" fill="none" stroke="#fff" stroke-width=".9"/></svg>
      <div class="fact-text" style="top:0"><p class="fact-value heading">6.000</p><p class="fact-label">ZUFRIEDENE KUNDEN*INNEN</p></div>
    </div>
    <div class="divider" style="top:206px"></div>
    <div class="fact body" style="top:229px">
      <svg width="30" height="30" viewBox="0 0 30 30" aria-hidden="true"><circle cx="14" cy="14" r="13.5" fill="none" stroke="#fff" stroke-width=".8"/><path d="M7 14 L13 21 L27 4" fill="none" stroke="#fff" stroke-width=".9"/></svg>
      <div class="fact-text" style="top:0"><p class="fact-value heading"><small>mehr als </small>90.000</p><p class="fact-label fact-label--plain">professionelle Behandlungen</p></div>
    </div>
  </section>

  <section class="window window--welcome">
    <div class="photo photo--treatment" role="img" aria-label="Foto: zwei lächelnde Kosmetikerinnen bereiten eine Behandlungsliege vor"></div>
    <div class="wax-badge">
      <svg width="128" height="128" viewBox="0 0 128 128" aria-hidden="true">
        <circle cx="64" cy="64" r="60" fill="none" stroke="var(--teal-light)" stroke-width=".6"/>
        <circle cx="64" cy="64" r="56" fill="none" stroke="var(--teal-light)" stroke-width=".6"/>
      </svg>
      <div class="wax-badge-core"><p class="heading">WE<br>WAX<br>YOU!</p></div>
    </div>
  </section>

  <section class="window window--smooth">
    <h2 class="smooth-title heading">GLATTE, SEXY HAUT<br>FÜR MEHRERE WOCHEN</h2>
    <div class="photo--friends" role="img" aria-label="Foto: drei Freundinnen liegen lachend auf dem Bett und strecken die Beine hoch"></div>
    <div class="brand-badge"><span>glattora</span></div>
  </section>

</main>
</body>
</html>
```